Thornwick Holdings, Inc.
dba Marigold Lagoon - It's How Fun Is Done!
Thornwick Holdings, Inc. -
Creative Brief
Ronald Malvern
CEO
PO Box 812 Washington, DC 20017
Rmalvern@marigoldlagoonfec.com
www.marigoldlagoonfec.com

```html
<!DOCTYPE html>
<html lang="en">
<head>
<meta charset="utf-8">
<title>Marigold Lagoon – Business Card</title>
<link rel="stylesheet" href="https://fonts.googleapis.com/css2?family=Open+Sans:wght@400;600;700&display=swap">
<style>
  :root {
    --backdrop: #e9e4dc;
    --card: #ffffff;
    --brand-blue: #1f6db5;
    --brand-red: #d9232a;
    --ink: #3a3a3a;
    --rule: #c9c9c9;
  }
  * { box-sizing: border-box; margin: 0; padding: 0; }
  html, body {
    width: 1200px; height: 780px; overflow: hidden;
    background: var(--backdrop);
    font-family: "Open Sans", sans-serif;
  }
  .card {
    position: absolute; left: 75px; top: 90px;
    width: 1050px; height: 600px;
    background: var(--card);
    border-radius: 36px;
    overflow: hidden;
    box-shadow: 0 6px 18px rgba(0,0,0,0.18);
  }
  .card__header { position: absolute; left: 0; top: 0; width: 1050px; height: 220px; }
  .holder { position: absolute; right: 60px; top: 28px; text-align: right; color: #fff; }
  .holder__name { font-size: 30px; font-weight: 700; line-height: 1.15; }
  .holder__title { font-size: 20px; font-weight: 400; }
  .brand {
    position: absolute; left: 40px; top: 300px; width: 370px;
    display: flex; align-items: center; justify-content: center; gap: 12px;
  }
  .brand__dot { width: 22px; height: 22px; border-radius: 50%; background: var(--brand-red); flex: none; }
  .brand__name { font-size: 34px; font-weight: 700; color: var(--brand-blue); white-space: nowrap; }
  .divider {
    position: absolute; left: 440px; top: 200px; width: 2px; height: 330px;
    background: linear-gradient(var(--card), var(--rule) 20%, var(--rule) 80%, var(--card));
  }
  .address {
    position: absolute; left: 480px; top: 190px;
    font-size: 22px; line-height: 1.4; color: var(--ink);
  }
  .contacts { position: absolute; left: 480px; top: 325px; list-style: none; }
  .contacts li {
    display: flex; align-items: center; gap: 14px;
    font-size: 21px; color: var(--ink); height: 38px;
  }
  .contacts svg { width: 24px; height: 24px; flex: none; }
</style>
</head>
<body>
  <div class="card">
    <svg class="card__header" viewBox="0 0 1050 220" aria-hidden="true">
      <path d="M0 0 H1050 V128 C820 150 560 200 300 190 C170 185 70 168 0 150 Z" fill="var(--brand-blue)"/>
      <path d="M0 150 C70 168 170 185 300 190 C560 200 820 150 1050 128" fill="none" stroke="#fff" stroke-width="8"/>
      <path d="M0 162 C90 190 200 205 320 206 C560 208 820 168 1050 140 L1050 152 C820 178 560 222 320 220 C200 219 90 200 0 172 Z" fill="var(--brand-red)"/>
    </svg>

    <div class="holder">
      <div class="holder__name">Ronald Malvern</div>
      <div class="holder__title">CEO</div>
    </div>

    <div class="brand">
      <span class="brand__dot"></span>
      <span class="brand__name">Marigold Lagoon</span>
    </div>

    <div class="divider"></div>

    <address class="address" style="font-style:normal">
      PO Box 812<br>Washington, DC 20017
    </address>

    <ul class="contacts">
      <li>
        <svg viewBox="0 0 24 24"><path d="M6 3 L9 3 L10.5 8 L8.5 9.5 C9.5 12 11.5 14 14 15.5 L15.5 13.5 L20.5 15 L20.5 18 C20.5 19.5 19 21 17 21 C10 20 4 14 3 7 C3 5 4.5 3 6 3 Z" fill="var(--brand-blue)"/></svg>
        202-555-0142
      </li>
      <li>
        <svg viewBox="0 0 24 24"><rect x="7" y="2" width="10" height="20" rx="2" fill="var(--brand-blue)"/><rect x="9" y="5" width="6" height="11" fill="#fff"/><circle cx="12" cy="19" r="1.2" fill="#fff"/></svg>
        202-555-0178
      </li>
      <li>
        <svg viewBox="0 0 24 24"><rect x="3" y="9" width="18" height="11" rx="2" fill="var(--brand-blue)"/><rect x="7" y="3" width="10" height="7" fill="none" stroke="var(--brand-blue)" stroke-width="2"/><rect x="7" y="14" width="10" height="2" fill="#fff"/></svg>
        202-555-0193
      </li>
      <li>
        <svg viewBox="0 0 24 24"><rect x="2" y="5" width="20" height="14" rx="2" fill="var(--brand-blue)"/><path d="M3 6 L12 13 L21 6" fill="none" stroke="#fff" stroke-width="1.8"/></svg>
        Rmalvern@marigoldlagoonfec.com
      </li>
      <li>
        <svg viewBox="0 0 24 24"><circle cx="12" cy="12" r="9" fill="none" stroke="var(--brand-blue)" stroke-width="2"/><ellipse cx="12" cy="12" rx="4" ry="9" fill="none" stroke="var(--brand-blue)" stroke-width="1.6"/><path d="M3 12 H21" stroke="var(--brand-blue)" stroke-width="1.6"/></svg>
        www.marigoldlagoonfec.com
      </li>
    </ul>
  </div>
</body>
</html>
```